Business Card Design Project

Looking for a logo and business card for a Real State Business i will be opening. The name is not choosen yet , but will probably be RTV IMOVEIS.
I was thinking black and silver colors, but am open to nice ideas.
I did add a business card that i liked a lot, am looking for something like that, with logo in black or silver in a black card. The logo i was thinking in the letters RTV as i uploaded or something or little and cute buildings or a house...just ideas, can be any nice logo.
Updates

You guys can add other colors if you want, I like colors very "BRIGHT" and "open", like red, pink, strong colors. almost glow in the dark colors. lol

Designers,

I've increased more 88 dollars in the budget for 1st place cause I will want envelope designs... small and big sizes.

So 1st place is now U$248,00. 

No need to send the envelope designs right now... only the business cards designs.

Thank you.

Industry/Entity Type

Business

Requirements
Must have
• Renata Tavares Vilela

www.RTVimoveis-exemplo.com.br

+554188316402

renata@rtvimoveis-exemplo.com.br

```html
<!DOCTYPE html>
<html lang="pt-BR">
<head>
<meta charset="utf-8">
<title>RTV IMOVEIS – Cartão de visita</title>
<link rel="stylesheet" href="https://fonts.googleapis.com/css2?family=Exo+2:wght@400;600;700&display=swap">
<style>
  :root {
    --backdrop: #3a3a3a;
    --card: #2b2b2b;
    --brand-dark: #141414;
    --pink: #e6007e;
    --city-dark: #0e0e0e;
    --city-light: #dcdcdc;
  }
  * { margin: 0; padding: 0; box-sizing: border-box; }
  html, body { width: 1200px; height: 900px; overflow: hidden; }
  body {
    background: var(--backdrop);
    font-family: "Exo 2", sans-serif;
    position: relative;
  }
  .card {
    position: absolute;
    top: 307px;
    width: 515px;
    height: 285px;
    background: var(--card);
    box-shadow: 0 2px 6px rgba(0,0,0,.45);
    overflow: hidden;
  }
  .card--front { left: 72px; }
  .card--back { left: 615px; }

  .front-brand {
    position: absolute;
    inset: 0;
    display: flex;
    align-items: center;
    justify-content: center;
    gap: 14px;
  }
  .front-brand__mark {
    width: 26px; height: 26px;
    background: var(--brand-dark);
  }
  .front-brand__name {
    font-weight: 700;
    font-size: 38px;
    letter-spacing: 1px;
    color: var(--brand-dark);
  }

  .back-brand {
    position: absolute;
    left: 52px; top: 128px;
    width: 200px;
    display: flex;
    align-items: center;
    gap: 8px;
  }
  .back-brand__mark {
    width: 14px; height: 14px;
    background: var(--pink);
  }
  .back-brand__name {
    font-weight: 700;
    font-size: 22px;
    letter-spacing: .5px;
    color: var(--pink);
  }
  .divider {
    position: absolute;
    left: 273px; top: 46px;
    width: 1px; height: 124px;
    background: var(--pink);
  }
  .contact {
    position: absolute;
    left: 300px; top: 56px;
    color: var(--pink);
  }
  .contact__name {
    font-weight: 600;
    font-size: 17px;
    letter-spacing: .3px;
    margin-bottom: 19px;
  }
  .contact__line {
    font-size: 12px;
    line-height: 14px;
    font-weight: 400;
  }
  .contact__line--phone { margin-bottom: 14px; }

  .city-art {
    position: absolute;
    left: 0; bottom: 0;
    width: 515px; height: 96px;
    background: linear-gradient(100deg, var(--city-dark) 0%, var(--city-dark) 50%, var(--city-light) 100%);
  }
</style>
</head>
<body>
  <section class="card card--front" aria-label="Frente do cartão">
    <div class="front-brand">
      <span class="front-brand__mark"></span>
      <span class="front-brand__name">RTV IMOVEIS</span>
    </div>
  </section>

  <section class="card card--back" aria-label="Verso do cartão">
    <div class="back-brand">
      <span class="back-brand__mark"></span>
      <span class="back-brand__name">RTV IMOVEIS</span>
    </div>
    <div class="divider"></div>
    <div class="contact">
      <p class="contact__name">Renata Tavares Vilela</p>
      <p class="contact__line contact__line--phone">+554 188 316 402</p>
      <p class="contact__line">renata@rtvimoveis-exemplo.com.br</p>
      <p class="contact__line">www.RTVimoveis-exemplo.com.br</p>
    </div>
    <div class="city-art" role="img" aria-label="Ilustração de silhueta de prédios da cidade"></div>
  </section>
</body>
</html>
```